Educational website design and repeat learning

The aim of the project is to create a learning platform to support high school students in their learning. It aims to integrate as much as possible the potential of digital tools (videos, navigation) in the educational path of students, in the acquisition of knowledge and its use. In particular, it will integrate a learning system in spaced repetition (flashcards).

The students are the central users of the platform. They must have access to the following features:
• Access to course content and the map review tool
• Personal dashboard, retracing the courses taken, the number of revised cards and other metrics
• A notification panel, suggesting to him the revision of such or such pack of cards, or of such or such concept in the rest of the contents

Flashcards are a learning system based on spaced repetition, on a format of cards associating a question and an answer. Ideally, each card involves only a limited amount of knowledge. The learner successively repeats the cards and associates with each of them a difficulty (or failure if necessary), leading the system to offer him, as a priority, the cards that are the most difficult for him.

Once the designer has been chosen, the site map and the wireframes will be transmitted to start work on the site code.
Updates

Les designs se ressemblent

Target Market(s)

High school students - France

Industry/Entity Type

Education

Logo Text

brio-slate

Coding

Coded - Design and coding required

Number of Pages Required

4 page

Font styles to use
Sans Serif

Requirements
Must have
• Must be offered:
- 1 design of home page, content (lorem ipsum), possibility of connection / registration
- 1 course sheet page design, with the complete course hierarchy
- 1 design of the spaced repetition tool
Nice to have
• - 1 student dashboard design with the following elements:
• Time spent on the platform (graph week by week + week in progress)
• Number of course sheets read (total and week)
• Number of cards revised (total and week)
Should not have
• Light blue

```html
<!DOCTYPE html>
<html lang="en">
<head>
<meta charset="utf-8">
<title>brio-slate — Section</title>
<link href="https://fonts.googleapis.com/css2?family=Lato:wght@400;700;900&display=swap" rel="stylesheet">
<style>
:root{
  --sidebar-bg:#f4f5f5;
  --page-bg:#ffffff;
  --brand:#27ae60;
  --nav-text:#444;
  --nav-active-bg:#e3f2e8;
  --heading:#777;
  --green:#27ae60;
  --blue:#0a8fe9;
  --orange:#ff8c00;
  --purple:#8e27ab;
  --blue-2:#0b7fd6;
  --crimson:#e0344a;
  --progress:#8fe823;
  --track:rgba(0,0,0,.12);
  --white:#fff;
}
*{box-sizing:border-box;margin:0;padding:0}
html,body{width:1200px;height:675px;overflow:hidden}
body{font-family:'Lato',sans-serif;background:var(--sidebar-bg);position:relative}
.sidebar{position:absolute;left:0;top:0;width:131px;height:675px;background:var(--sidebar-bg)}
.brand{position:absolute;left:18px;top:34px;font-family:'Lato',sans-serif;font-weight:900;font-size:18px;color:var(--brand);letter-spacing:.3px;display:flex;align-items:center;gap:6px}
.brand-mark{width:9px;height:9px;background:var(--brand);border-radius:2px}
.nav{list-style:none}
.nav-item{position:absolute;left:0;width:131px;height:32px;display:flex;align-items:center;padding-left:15px;gap:8px;font-size:9px;color:var(--nav-text)}
.nav-item svg{width:11px;height:11px;flex:none}
.nav-item.active{background:var(--nav-active-bg);color:var(--brand);border-left:3px solid var(--brand);padding-left:12px}
.main{position:absolute;left:131px;top:0;width:1069px;height:675px;background:var(--page-bg);border-top-left-radius:24px}
.section-title{position:absolute;left:43px;top:28px;font-size:25px;font-weight:700;color:var(--heading);letter-spacing:3px}
.card{position:absolute;width:476px;height:179px;border-radius:12px;color:var(--white);box-shadow:0 2px 6px rgba(0,0,0,.12)}
.card-title{position:absolute;left:38px;top:36px;font-size:26px;font-weight:900;letter-spacing:2px;line-height:1}
.card-text{position:absolute;left:38px;top:65px;font-size:11.3px;font-weight:700;letter-spacing:1.05px;line-height:14px}
.play-btn{position:absolute;left:38px;top:132px;width:182px;height:31px;border-radius:16px;background:var(--white);color:var(--green);font-size:11.5px;font-weight:700;letter-spacing:1px;display:flex;align-items:center;justify-content:center}
.progress{position:absolute;left:238px;top:143px;width:220px;height:11px;border-radius:6px;background:var(--track);overflow:hidden}
.progress-fill{height:100%;border-radius:6px;background:var(--progress)}
.card--green{background:var(--green)}
.card--blue{background:var(--blue)}
.card--orange{background:var(--orange)}
.card--purple{background:var(--purple)}
.card--blue-2{background:var(--blue-2)}
.card--crimson{background:var(--crimson)}
</style>
</head>
<body>
<aside class="sidebar">
  <div class="brand"><span>brio-slate</span><span class="brand-mark"></span></div>
  <ul class="nav">
    <li class="nav-item active" style="top:84px"><svg viewBox="0 0 12 12" fill="none" stroke="currentColor" stroke-width="1.4"><path d="M1.5 6 6 1.8 10.5 6M3 5v5.3h6V5"/></svg>Home</li>
    <li class="nav-item" style="top:121px"><svg viewBox="0 0 12 12" fill="#444"><rect x="1" y="7" width="2" height="4"/><rect x="5" y="2" width="2" height="9"/><rect x="9" y="5" width="2" height="6"/></svg>Dashboard</li>
    <li class="nav-item" style="top:158px"><svg viewBox="0 0 12 12"><path d="M6 1.5a3.2 3.2 0 0 0-3.2 3.2V8L1.6 9.5h8.8L9.2 8V4.7A3.2 3.2 0 0 0 6 1.5zM4.8 10.3a1.2 1.2 0 0 0 2.4 0z" fill="#444"/><circle cx="9.8" cy="1.8" r="1.6" fill="#ff8c00"/></svg>Notifications</li>
    <li class="nav-item" style="top:200px"><svg viewBox="0 0 12 12" fill="none" stroke="#444" stroke-width="1.3"><circle cx="6" cy="4" r="2.3"/><path d="M1.8 11c.4-2.4 2.1-3.6 4.2-3.6s3.8 1.2 4.2 3.6z"/></svg>Profile</li>
    <li class="nav-item" style="top:337px"><svg viewBox="0 0 12 12" fill="none" stroke="#444" stroke-width="1.6"><circle cx="6" cy="6" r="4.6"/><circle cx="6" cy="6" r="1.8"/></svg>Help Center</li>
    <li class="nav-item" style="top:374px"><svg viewBox="0 0 12 12"><circle cx="6" cy="6" r="4" fill="none" stroke="#444" stroke-width="2.4" stroke-dasharray="2 1.2"/><circle cx="6" cy="6" r="2.6" fill="#444"/><circle cx="6" cy="6" r="1.2" fill="#f4f5f5"/></svg>Settings</li>
    <li class="nav-item" style="top:410px"><svg viewBox="0 0 12 12" fill="none" stroke="#444" stroke-width="1.2"><path d="M7.5 3V1.5h-5.5v9h5.5V9M5 6h6M9 4l2 2-2 2"/></svg>Exit</li>
  </ul>
</aside>

<main class="main">
  <h1 class="section-title">Section</h1>

  <article class="card card--green" style="left:45px;top:73px">
    <h2 class="card-title">Subject Title</h2>
    <p class="card-text">Lorem Ipsum Dolor Sit Amet,<br>&nbsp;Consectetur Adipisicing Elit, Sed Do Eiusmod<br>Tempor Incididunt Ut</p>
    <div class="play-btn">PLAY</div>
    <div class="progress"><div class="progress-fill" style="width:85%"></div></div>
  </article>

  <article class="card card--blue" style="left:543px;top:73px">
    <h2 class="card-title">Subject Title</h2>
    <p class="card-text">Lorem Ipsum Dolor Sit Amet,<br>&nbsp;Consectetur Adipisicing Elit, Sed Do Eiusmod<br>Tempor Incididunt Ut</p>
    <div class="play-btn">PLAY</div>
    <div class="progress"><div class="progress-fill" style="width:22%"></div></div>
  </article>

  <article class="card card--orange" style="left:45px;top:272px">
    <h2 class="card-title">Subject Title</h2>
    <p class="card-text">Lorem Ipsum Dolor Sit Amet,<br>&nbsp;Consectetur Adipisicing Elit, Sed Do Eiusmod<br>Tempor Incididunt Ut</p>
    <div class="play-btn">PLAY</div>
    <div class="progress"><div class="progress-fill" style="width:22%"></div></div>
  </article>

  <article class="card card--purple" style="left:543px;top:272px">
    <h2 class="card-title">Subject Title</h2>
    <p class="card-text">Lorem Ipsum Dolor Sit Amet,<br>&nbsp;Consectetur Adipisicing Elit, Sed Do Eiusmod<br>Tempor Incididunt Ut</p>
    <div class="play-btn">PLAY</div>
    <div class="progress"><div class="progress-fill" style="width:50%"></div></div>
  </article>

  <article class="card card--blue-2" style="left:45px;top:472px">
    <h2 class="card-title">Subject Title</h2>
    <p class="card-text">Lorem Ipsum Dolor Sit Amet,<br>&nbsp;Consectetur Adipisicing Elit, Sed Do Eiusmod<br>Tempor Incididunt Ut</p>
    <div class="play-btn">PLAY</div>
    <div class="progress"><div class="progress-fill" style="width:22%"></div></div>
  </article>

  <article class="card card--crimson" style="left:543px;top:472px">
    <h2 class="card-title">Subject Title</h2>
    <p class="card-text">Lorem Ipsum Dolor Sit Amet,<br>&nbsp;Consectetur Adipisicing Elit, Sed Do Eiusmod<br>Tempor Incididunt Ut</p>
    <div class="play-btn">PLAY</div>
    <div class="progress"><div class="progress-fill" style="width:22%"></div></div>
  </article>
</main>
</body>
</html>
```